Business Card Project for Firm Deck Hoisting

Business name is "Firm Deck Hoisting" we are a scaffolding & rigging business specialising in local and remote work for:
- scaffolding (residential, commercial, industrial)
- rigging
-man material hoists
- swing stages
- labour hire

On the back of the card I would like FDH as the symbol / logo. I have attached the logos we have had created by sketch harbour. We would like to use bold colours – preferably as the same colour scheme as the logo.

Target Market(s)

Construction business

Industry/Entity Type

Construction

Contact Information for Business Card

name: Owen Pellew
Title: Director
Phone: 0491 572 864
Address: PO BOX 3251, Kestrel Vale SA 5199
Email: owen@firmdeckhoisting.com.au
Website: www.firmdeckhoisting.com.au

Font styles to use
Sans Serif

Requirements
Must have
• Must use existing logo & prefering using bold colours
Nice to have
• Would be nice to have a line of dot points in what we specialise in but not essential
• Would be nice to see some designs with a slogan but not essential
Should not have
• NA

```html
<!DOCTYPE html>
<html lang="en">
<head>
<meta charset="utf-8">
<title>Firm Deck Hoisting — Business Card</title>
<link rel="stylesheet" href="https://fonts.googleapis.com/css2?family=Roboto:wght@400;500;700&display=swap">
<style>
  :root {
    --backdrop: #5c3d2d;
    --card-dark: #231f20;
    --card-light: #ffffff;
    --brand-blue: #2a7bc0;
    --text-light: #ffffff;
    --card-shadow: 0 6px 18px rgba(0,0,0,0.45);
  }
  * { margin: 0; padding: 0; box-sizing: border-box; }
  html, body {
    width: 1200px; height: 1000px; overflow: hidden;
    background: var(--backdrop);
    font-family: "Roboto", Arial, sans-serif;
  }
  .canvas { position: relative; width: 1200px; height: 1000px; }

  .card {
    position: absolute; left: 288px; width: 626px; height: 360px;
    box-shadow: var(--card-shadow);
  }
  .card-front { top: 140px; background: var(--card-dark); }
  .card-back { top: 531px; height: 359px; display: flex; }

  /* Front */
  .brand-word {
    position: absolute; left: 100px; top: 130px;
    font-weight: 700; font-size: 92px; line-height: 1;
    letter-spacing: -2px; color: var(--text-light);
  }
  .front-divider {
    position: absolute; left: 344px; top: 122px;
    width: 1px; height: 114px; background: var(--brand-blue);
  }
  .services {
    position: absolute; left: 370px; top: 115px; list-style: none;
  }
  .services li {
    position: relative; padding-left: 18px;
    font-size: 15px; line-height: 26px; color: var(--text-light);
  }
  .services li::before {
    content: ""; position: absolute; left: 0; top: 9px;
    width: 8px; height: 8px; border-radius: 50%;
    background: var(--brand-blue);
  }

  /* Back: contact side */
  .contact-side {
    position: relative; width: 312px; height: 100%;
    background: var(--card-dark); color: var(--text-light);
  }
  .accent-bar {
    position: absolute; left: 0; top: 43px;
    width: 8px; height: 83px; background: var(--brand-blue);
  }
  .person { position: absolute; left: 39px; top: 39px; }
  .person-name {
    font-size: 18px; font-weight: 500; color: var(--brand-blue); line-height: 22px;
  }
  .person-title { font-size: 14px; line-height: 20px; margin-top: 1px; }
  .contact-lines { margin-top: 8px; font-size: 15px; line-height: 21px; }
  .contact-lines .label { color: var(--brand-blue); }

  .company { position: absolute; left: 39px; top: 262px; font-size: 15px; }
  .company-name { color: var(--brand-blue); line-height: 21px; }
  .company-address { line-height: 21px; }
  .company-web { line-height: 21px; margin-top: 4px; }

  /* Back: brand side */
  .brand-side {
    width: 314px; height: 100%; background: var(--card-light);
    display: flex; align-items: center; justify-content: center;
  }
  .brand-name {
    font-weight: 700; font-size: 24px; color: var(--card-dark);
    letter-spacing: 0.2px;
  }
</style>
</head>
<body>
<main class="canvas">
  <section class="card card-front">
    <div class="brand-word">FDH</div>
    <div class="front-divider"></div>
    <ul class="services">
      <li>Scaffolding</li>
      <li>Rigging</li>
      <li>Man material hoists</li>
      <li>Swing stages</li>
      <li>Labour hire</li>
    </ul>
  </section>

  <section class="card card-back">
    <div class="contact-side">
      <div class="accent-bar"></div>
      <div class="person">
        <p class="person-name">Owen Pellew</p>
        <p class="person-title">Director</p>
        <div class="contact-lines">
          <p><span class="label">P</span> : 0491 572 864</p>
          <p><span class="label">E</span> : owen@firmdeckhoisting.com.au</p>
        </div>
      </div>
      <div class="company">
        <p class="company-name">Firm Deck Hoisting</p>
        <p class="company-address">PO BOX 3251, Kestrel Vale SA 5199</p>
        <p class="company-web">www.firmdeckhoisting.com.au</p>
      </div>
    </div>
    <div class="brand-side">
      <span class="brand-name">Firm Deck Hoisting</span>
    </div>
  </section>
</main>
</body>
</html>
```